Not your average candle company needs label design

MOSS + RUIN A Brand Deck for Disruptive Candles
WHO WE ARE
Moss + Ruin is a disruptive candle brand built on contrast. We create clean-burning, scent-forward rituals for people who are both grounded and undone.
We’re not here for the beige wellness aesthetic. We’re here for the moments that are messy, bold, emotional, and beautifully real.
Rooted in botanical craftsmanship. Branded in poetic defiance.
WHAT WE WANT PEOPLE TO THINK
When someone encounters Moss + Ruin, we want them to feel like they’ve stumbled into something intimate, moody, and unforgettable.
We want them to think:
• “This brand gets me.”
• “This feels like design, emotion, and scent in one.”
• “It’s art I can burn.”
• “I’ve never seen a candle brand like this before.”
Our name alone sparks curiosity. Our story keeps them. Our product delivers.

Target Market(s)

Women and men ages 25–45 who appreciate thoughtful design and emotional storytelling People who love brands like Farvale, Kid Whiffs, Pelican Grange, Mivune, and Du Vanto Design-minded buyers who shop indie, high-end, or artisanal and care about self-expression through scent Emotionally intelligent rebels. Introspective, edgy, but craving grounding rituals.

Industry/Entity Type

Candle Industry

Font styles to use
Other font styles liked:
• Moss should be more refined in a serif font and I like mistrully font for ruin.

Requirements
Must have
• Space for scent name and optionally, a small poetic tagline (like still roots. wild glow.) Layout that’s elegant but with tension — surprise us with something that doesn't play it safe Optional: room for batch no., burn time, scent notes on side or bottom. MOSS + RUIN still roots. wild glow. Scent name example: Lanternfall A silent vow to stay grounded. Earthy and grounding — like old books, soft shadows, and the quiet certainty of knowing who you are. [optional: 7 oz / 198g | coconut soy wax | 45+ hr burn time]
Nice to have
• raw edge opening with gold font. Open to colored labels. We’re creating an unforgettable candle brand called Moss + Ruin — a contrast-rich, emotionally resonant collection of candles that blend botanical beauty with bold edge. The name is intentional: Moss reflects grounding, ritual, and plant-based purity; Ruin speaks to vulnerability, chaos, and strength through contrast. Our brand is not dark or gothic — it’s confident, elevated, and style-forward, with packaging that feels like a cross between modern apothecary and high fashion. Think Mivune meets Dale Pruitt. Gloss vessels, textured labels, contrasting fonts, and emotional scent storytelling.
Should not have
• goth vibe, typical candle label template layout.

```html
<!DOCTYPE html>
<html lang="en">
<head>
<meta charset="utf-8">
<title>Moss + Ruin — Lanternfall label</title>
<link rel="stylesheet" href="https://fonts.googleapis.com/css2?family=Playfair+Display:wght@400&family=Caveat:wght@500&family=Montserrat:wght@300&display=swap">
<style>
  :root {
    --page: #ffffff;
    --label-paper: #f3f3f3;
    --copper: #c4966b;
  }
  html, body {
    margin: 0;
    padding: 0;
    width: 1200px;
    height: 864px;
    overflow: hidden;
    background: var(--page);
  }
  .canvas {
    position: relative;
    width: 1200px;
    height: 864px;
  }
  .label {
    position: absolute;
    left: 300px;
    top: 132px;
    width: 600px;
    height: 600px;
    display: block;
  }
  .label-paper { fill: var(--label-paper); }
  .frame-line, .seal-ring {
    fill: none;
    stroke: var(--copper);
    stroke-width: 1.6;
  }
  .rule-taper { fill: var(--copper); }
  .brand-name {
    font-family: "Playfair Display", Georgia, serif;
    font-weight: 400;
    font-size: 58px;
    fill: var(--copper);
  }
  .scent-name {
    font-family: "Playfair Display", Georgia, serif;
    font-size: 29px;
    letter-spacing: 4px;
    fill: var(--copper);
  }
  .tagline {
    font-family: "Caveat", cursive;
    font-weight: 500;
    font-size: 38px;
    fill: var(--copper);
  }
  .net-weight {
    font-family: "Montserrat", Arial, sans-serif;
    font-weight: 300;
    font-size: 18px;
    fill: var(--copper);
  }
</style>
</head>
<body>
<main class="canvas">
  <svg class="label" viewBox="0 0 568 568" xmlns="http://www.w3.org/2000/svg">
    <rect class="label-paper" x="0" y="0" width="568" height="568"/>

    <path class="frame-line" d="M20,0 V218 Q20,262 25,283 Q20,304 20,348 V568"/>
    <path class="frame-line" d="M548,0 V218 Q548,262 543,283 Q548,304 548,348 V568"/>

    <ellipse class="seal-ring" cx="284" cy="284" rx="259" ry="200"/>

    <text class="brand-name" x="284" y="266" text-anchor="middle" textLength="400" lengthAdjust="spacingAndGlyphs">MOSS + RUIN</text>

    <text class="scent-name" x="284" y="324" text-anchor="middle">LANTERNFALL</text>

    <path class="rule-taper" d="M170,342 Q285,339.6 400,342 Q285,344.4 170,342 Z"/>

    <text class="tagline" x="284" y="383" text-anchor="middle">still roots. wild glow.</text>

    <text class="net-weight" x="284" y="554" text-anchor="middle">7,5oz-212g</text>
  </svg>
</main>
</body>
</html>
```